modern real estate design
business card/letterhead/envelop
Dorian Parks
President
408 W Birch Avenue Belle Plaine, MN 56093
dorian@tidewaterhomesgroup.com
www.tidewaterhomesgroup.com
Licensed Realtor with Quiet Harbor Real Estate
Escape Gravity.
newell343 newell343
I am also interested in getting a design done for metal business cards. It would be cool to have them die cut, etched, and have our two color logo on them. Thanks.

```html
<!DOCTYPE html>
<html lang="en">
<head>
<meta charset="utf-8">
<title>Tidewater Homes Group – Business Card</title>
<link href="https://fonts.googleapis.com/css2?family=Montserrat:wght@500;600;700&family=Open+Sans:wght@400;600&display=swap" rel="stylesheet">
<style>
  :root {
    --backdrop: #2b2c2f;
    --card-white: #ffffff;
    --card-grey: #8d9094;
    --teal: #2bb6c1;
    --navy: #1f3a6e;
    --magenta: #d6286e;
    --logo-grey: #6f7378;
    --text-light: #ffffff;
  }
  * { margin: 0; padding: 0; box-sizing: border-box; }
  html, body { width: 1200px; height: 646px; overflow: hidden; }
  body {
    background: var(--backdrop);
    font-family: "Open Sans", sans-serif;
    position: relative;
  }
  .card {
    position: absolute;
    top: 170px;
    width: 540px;
    height: 306px;
    border-radius: 16px;
    overflow: hidden;
    background: var(--card-white);
  }
  .card--front { left: 40px; }
  .card--back { left: 620px; }

  .brand {
    position: absolute;
    display: flex;
    align-items: center;
    gap: 12px;
    font-family: "Montserrat", sans-serif;
    font-weight: 700;
    letter-spacing: 1.5px;
    line-height: 1.1;
    color: var(--logo-grey);
  }
  .brand__dot {
    width: 34px; height: 34px;
    border-radius: 50%;
    background: var(--teal);
    flex: none;
  }
  .card--front .brand { left: 70px; top: 124px; font-size: 26px; }
  .card--back .brand { left: 36px; top: 116px; font-size: 19px; }
  .card--back .brand__dot { width: 26px; height: 26px; }

  .card__swoosh { position: absolute; inset: 0; width: 100%; height: 100%; }

  .person {
    position: absolute;
    right: 22px; top: 20px;
    text-align: right;
    font-family: "Montserrat", sans-serif;
  }
  .person__name { font-size: 17px; font-weight: 700; color: var(--navy); }
  .person__title { font-size: 14px; font-weight: 500; color: var(--magenta); margin-top: 2px; }

  .contact {
    position: absolute;
    left: 26px; bottom: 14px;
    color: var(--text-light);
    font-size: 11px;
    line-height: 1.55;
  }
  .phones {
    position: absolute;
    right: 22px; bottom: 88px;
    color: var(--text-light);
    font-size: 11px;
    line-height: 1.6;
    text-align: right;
  }
</style>
</head>
<body>

  <section class="card card--front" aria-label="Card front">
    <div class="brand">
      <span class="brand__dot"></span>
      <span>TIDEWATER<br>HOMES GROUP</span>
    </div>
  </section>

  <section class="card card--back" aria-label="Card back">
    <svg class="card__swoosh" viewBox="0 0 540 306" preserveAspectRatio="none" aria-hidden="true">
      <path d="M0,186 C200,226 400,176 540,36 L540,306 L0,306 Z" fill="var(--teal)"/>
      <path d="M0,202 C205,238 405,194 540,60 L540,306 L0,306 Z" fill="#ffffff"/>
      <path d="M0,212 C210,248 410,206 540,80 L540,306 L0,306 Z" fill="var(--card-grey)"/>
    </svg>

    <div class="person">
      <div class="person__name">Dorian Parks</div>
      <div class="person__title">President</div>
    </div>

    <div class="brand">
      <span class="brand__dot"></span>
      <span>TIDEWATER<br>HOMES GROUP</span>
    </div>

    <div class="phones">
      <div>P: 612 555 0148</div>
      <div>C: 612 555 0148</div>
    </div>

    <div class="contact">
      <div>dorian@tidewaterhomesgroup.com</div>
      <div>www.tidewaterhomesgroup.com</div>
      <div>408 W Birch Avenue Belle Plaine, MN 56093</div>
    </div>
  </section>

</body>
</html>
```